Business Card Design for New Game Studio

We need a business card design. We are a new company developing innovative mobile and platform games.

I would like to see very innovative design thats brings out the company's goal and direction.

My Company's goal and direction is to "Evolve the way of gaming, Bring fun and entertainment to all gamers"

Please do use our company logo which I have attached to be included in the design.

Please put in details for name, title, contacts etc ... be creative !!!

Reason: Company logo redesign. Awaiting it. Thanks

Hi all Please do wait for my updated company logo. Thanks

Reason: Still waiting on new company logo. Thanks all

Hi All Designers .... Sorry for the long wait... Please see the new file for my new company logo uploaded. Waiting to see all your creative design. Cheers

Hi All .... Please do not just mass send a whole bunch of similar designs .... Would like to see quality instead of quantity Cheers

Entertainment

```html
<!DOCTYPE html>
<html lang="en">
<head>
<meta charset="utf-8">
<title>Emberstone Worlds – Business Card</title>
<link rel="stylesheet" href="https://fonts.googleapis.com/css2?family=Lato:wght@400;700;900&display=swap">
<style>
  :root {
    --backdrop: #e6e6e6;
    --paper: #f7f7f5;
    --ink: #2b2b2b;
    --ink-soft: #3a3a3a;
    --teal: #3e5d5e;
    --teal-deep: #274a4c;
    --green: #7fb24a;
    --charcoal: #4a4a4c;
  }
  * { margin: 0; padding: 0; box-sizing: border-box; }
  html, body {
    width: 1200px; height: 720px; overflow: hidden;
    background: var(--backdrop);
    font-family: "Lato", Arial, sans-serif;
  }
  .canvas { position: relative; width: 1200px; height: 720px; }
  .card {
    position: absolute; top: 240px;
    width: 420px; height: 241px;
    background: var(--paper);
    overflow: hidden;
  }
  .card--front { left: 147px; }
  .card--back { left: 634px; }
  .card__art { position: absolute; inset: 0; width: 420px; height: 241px; }

  .contact { position: absolute; left: 38px; top: 44px; color: var(--ink); }
  .contact__name { font-size: 14px; font-weight: 900; color: var(--teal); line-height: 1.1; }
  .contact__title { font-size: 10.5px; margin-top: 1px; }
  .contact__address { font-size: 10.5px; line-height: 1.25; margin-top: 12px; }
  .contact__list { list-style: none; margin-top: 12px; font-size: 10.5px; line-height: 12px; }
  .contact__list li { display: flex; align-items: center; gap: 7px; }
  .contact__icon { width: 10px; height: 10px; fill: var(--ink-soft); flex: none; }

  .brand {
    position: absolute; left: 0; right: 0; top: 110px;
    display: flex; align-items: center; justify-content: center; gap: 8px;
    padding-left: 110px;
  }
  .brand__dot { width: 16px; height: 16px; border-radius: 50%; background: var(--green); }
  .brand__name { font-size: 19px; font-weight: 900; color: var(--teal); letter-spacing: 0.5px; white-space: nowrap; }
</style>
</head>
<body>
<main class="canvas">

  <section class="card card--front" aria-label="Card front">
    <svg class="card__art" viewBox="0 0 420 241" aria-hidden="true">
      <defs>
        <linearGradient id="hillFill" x1="0" y1="0" x2="1" y2="0">
          <stop offset="0" stop-color="#274a4c"/>
          <stop offset="0.45" stop-color="#7fb24a"/>
          <stop offset="0.8" stop-color="#3e6a66"/>
        </linearGradient>
        <radialGradient id="emblemFill" cx="0.5" cy="0.5" r="0.5">
          <stop offset="0" stop-color="#8cc04f"/>
          <stop offset="0.55" stop-color="#4f7a6a"/>
          <stop offset="0.75" stop-color="#4a4a4c"/>
        </radialGradient>
      </defs>
      <path d="M0 186 C60 240 150 236 210 206 S310 156 350 156 L420 156 L420 241 L0 241 Z" fill="url(#hillFill)"/>
      <path d="M0 164 C50 222 150 228 214 196" fill="none" stroke="#fff" stroke-width="9"/>
      <path d="M0 164 C50 222 150 228 214 196" fill="none" stroke="#1e1e1e" stroke-width="5"/>
      <circle cx="420" cy="120" r="118" fill="#fff"/>
      <circle cx="420" cy="120" r="112" fill="url(#emblemFill)" role="img" aria-label="Brand emblem area"/>
    </svg>
    <div class="contact">
      <p class="contact__name">Lena Marsh</p>
      <p class="contact__title">Manager</p>
      <p class="contact__address">Here your company or<br>home address</p>
      <ul class="contact__list">
        <li><svg class="contact__icon" viewBox="0 0 10 10"><path d="M1 3c0-1 1-2 4-2s4 1 4 2v1H7V3H3v1H1zM2 5h6l1 4H1z"/></svg>312 5550 148</li>
        <li><svg class="contact__icon" viewBox="0 0 10 10"><path d="M3 0h4a1 1 0 0 1 1 1v8a1 1 0 0 1-1 1H3a1 1 0 0 1-1-1V1a1 1 0 0 1 1-1zm0 1.5v6h4v-6z"/></svg>+44 5550 1234</li>
        <li><svg class="contact__icon" viewBox="0 0 10 10"><path d="M0 2h10v6H0zm1 1 4 3 4-3v-0.2H1z"/></svg>hello@emberstoneworlds.com</li>
        <li><svg class="contact__icon" viewBox="0 0 10 10"><path d="M0 1h10v6H6v1h1v1H3V8h1V7H0zm1 1v4h8V2z"/></svg>www.emberstoneworlds.com</li>
      </ul>
    </div>
  </section>

  <section class="card card--back" aria-label="Card back">
    <svg class="card__art" viewBox="0 0 420 241" aria-hidden="true">
      <defs>
        <radialGradient id="emblemFillBack" cx="0.5" cy="0.5" r="0.5">
          <stop offset="0" stop-color="#8cc04f"/>
          <stop offset="0.55" stop-color="#4f7a6a"/>
          <stop offset="0.75" stop-color="#4a4a4c"/>
        </radialGradient>
      </defs>
      <circle cx="0" cy="120" r="112" fill="url(#emblemFillBack)" role="img" aria-label="Brand emblem area"/>
    </svg>
    <div class="brand">
      <span class="brand__dot"></span>
      <span class="brand__name">Emberstone Worlds</span>
    </div>
  </section>

</main>
</body>
</html>
```